Flyer for an online formula one racing league

Hello.

I am looking for the perfect one page facebook/instagram style flyer for an online formula one racing league. The racing league is called 'VOLKA RACING LEAGUE'.

Information that MUST be on the new flyer is already on the old flyer I have uploaded here. In addition to including: The Volka racing league 'R' logo I have uploaded AND the text: 'Very popular, clean and competitive racing league, running for its 4th season. Why not join with a friend? Race times, Mondays, Tuesdays and Wednesdays each at 8pm UK TIME Message below for any questions. (Spacing of information is not important, however all the information in regards to the racing I have just mentioned MUST BE on the flyer, this includes info from old pic, logo and the other info I just mentioned).

It would be beneficial to have lots of dark blue on the flyer and the new flyer to be a lot different to the original flyer I uploaded, but this is not essential.

I apologise if I did not explain very well, any questions, please message me.

The best flyer should look the most attractive to someone that might be interested in joining an online formula one racing league.

I used this website before to create the perfect logo for my Sunday League team last year, and I was very impressed. I look forward to seeing your submissions.

Target Market(s)

No specific target, more something that may attract someone into joining a formula one online racing league

Industry/Entity Type

e sports/formula one

Colors
0054AA
0677BA
7BADD7
CADEEF
E8F1F8

Requirements
Must have
• Read product description please
Should not have
• Ignoring product description!

```html
<!DOCTYPE html>
<html lang="en">
<head>
<meta charset="utf-8">
<title>Volka Racing League – New Season</title>
<link href="https://fonts.googleapis.com/css2?family=Monoton&family=Jost:wght@400;500&display=swap" rel="stylesheet">
<style>
  :root {
    --blue: #0054AA;
    --blue-mid: #0A5BB5;
    --pale: #CADEEF;
    --navy: #000C33;
    --white: #FFFFFF;
    --ink: #333A44;
  }
  html, body {
    margin: 0;
    padding: 0;
    overflow: hidden;
  }
  .flyer {
    position: relative;
    width: 1200px;
    height: 628px;
    overflow: hidden;
    background: radial-gradient(ellipse at 55% 45%, var(--blue-mid), var(--blue) 75%);
    font-family: "Jost", sans-serif;
    color: var(--white);
  }
  .crest-tab {
    position: absolute;
    left: 429px;
    top: -10px;
    width: 358px;
    height: 241px;
    background: var(--pale);
    border-radius: 0 0 179px 179px;
  }
  .crest {
    position: absolute;
    left: 527px;
    top: 22px;
    width: 163px;
    height: 163px;
    border-radius: 50%;
    background: var(--navy);
    display: flex;
    align-items: center;
    justify-content: center;
    font-family: "Jost", sans-serif;
    font-weight: 500;
    font-size: 34px;
    letter-spacing: 2px;
    color: var(--white);
  }
  .title {
    position: absolute;
    left: 20px;
    top: 96px;
    width: 485px;
    margin: 0;
    text-align: center;
    font-family: "Monoton", sans-serif;
    font-weight: 400;
    line-height: 93px;
    color: var(--white);
  }
  .title span { display: block; }
  .title .title-name { font-size: 72px; }
  .title .title-word { font-size: 80px; }
  .intro {
    position: absolute;
    left: 40px;
    top: 408px;
    width: 445px;
    margin: 0;
    text-align: center;
    font-size: 31px;
    line-height: 40px;
    letter-spacing: 1px;
  }
  .headline {
    position: absolute;
    left: 740px;
    top: 205px;
    width: 390px;
    margin: 0;
    text-align: center;
    font-size: 45px;
    font-weight: 500;
    line-height: 61px;
  }
  .details {
    position: absolute;
    left: 755px;
    top: 365px;
    width: 385px;
    margin: 0;
    text-align: center;
    font-size: 21.5px;
    line-height: 31px;
    letter-spacing: 0.4px;
  }
  .footer {
    position: absolute;
    left: 0;
    bottom: 0;
    width: 1200px;
    height: 61px;
    background: var(--pale);
    color: var(--ink);
  }
  .footer-car {
    position: absolute;
    left: 289px;
    top: 23px;
    width: 95px;
    height: 20px;
    border-radius: 10px;
    background: #2A2F38;
  }
  .footer-info {
    position: absolute;
    left: 420px;
    top: 0;
    margin: 0;
    line-height: 61px;
    font-size: 21px;
    letter-spacing: 0.6px;
    white-space: nowrap;
  }
  .footer-info .gap { display: inline-block; width: 18px; }
</style>
</head>
<body>
<div class="flyer">
  <div class="crest-tab"></div>
  <div class="crest">VOLKA</div>

  <h1 class="title">
    <span class="title-name">VOLKA</span>
    <span class="title-word">RACING</span>
    <span class="title-word">LEAGUE</span>
  </h1>

  <p class="intro">Very popular, clean and competitive racing league, running for its 4th season.</p>

  <h2 class="headline">New Season just starting!</h2>

  <p class="details">
    Why not join with a friend?<br>
    Race times - Mondays, Tuesdays and Wednesdays<br>
    at 8pm UK TIME<br>
    Message below for any questions...
  </p>

  <footer class="footer">
    <div class="footer-car" role="img" aria-label="Vintage racing car illustration"></div>
    <p class="footer-info">For more info : www.volkaleague.com<span class="gap"></span>team@volkaleague.com</p>
  </footer>
</div>
</body>
</html>
```